NEW Modern Sleek Business Card for VR Language Startup

Our startup is using VR to lead the next wave of world language education. We need a two-sided business card that introduces the larger organization (Quorvel Language Inc) and our contact info on one side and shows the product, Lumidrasca, on the other side.

Side 1 (contact info)= Quorvel Logo and Contact info (name, title, phone, email)

Side 2 (product)= Lumidrasc logo, text, and website
Text= Culturally Immersive Language Learning Games
Website= www.lumidrasc.example

Target Market(s)

Education, Technology

Contact Information for Business Card

Contact info will be updated upon approval of the design. For now, put this as a placeholder.

Perry Hollins
Founder & CEO
phollins@mailtrove.example
(555)-014-2736

Font styles to use
Other font styles liked:
• Gibson and Century Gothic are the brand fonts

Requirements
Nice to have
• I would love to see cohesion between the design and colors of the two logos. I have attached a few business card designs that I like, so you can get a feel for my preferred style.

```html
<!DOCTYPE html>
<html lang="en">
<head>
<meta charset="utf-8">
<title>Quorvel Language — Business Card</title>
<link href="https://fonts.googleapis.com/css2?family=Lato:wght@400;700&display=swap" rel="stylesheet">
<style>
  :root {
    --backdrop: #5c5c5c;
    --card: #000000;
    --white: #ffffff;
    --warm: #e8475a;
    --cool: #5b6fc9;
    --sky: #3ec3ec;
    --grey-text: #8c8c8c;
    --rule: #5a5a5a;
    --mark-warm: #ee6a4f;
    --mark-cool: #3fb4ea;
  }
  * { margin: 0; padding: 0; box-sizing: border-box; }
  html, body { width: 1200px; height: 960px; overflow: hidden; }
  body {
    background: var(--backdrop);
    font-family: "Lato", sans-serif;
    position: relative;
  }
  .card {
    position: absolute;
    top: 177px;
    width: 364px;
    height: 637px;
    background: var(--card);
    border-radius: 30px;
    box-shadow: 0 6px 18px rgba(0,0,0,0.35);
    color: var(--white);
    text-align: center;
  }
  .card--contact { left: 168px; }
  .card--product { left: 662px; }

  .brand-dot {
    position: absolute;
    left: 50%;
    border-radius: 50%;
    transform: translateX(-50%);
  }
  .card--contact .brand-dot { top: 115px; width: 88px; height: 88px; background: var(--mark-warm); }
  .card--product .brand-dot { top: 128px; width: 110px; height: 110px; background: var(--mark-cool); }

  .wordmark {
    position: absolute;
    left: 0; right: 0;
    font-weight: 700;
    color: var(--white);
    line-height: 1;
  }
  .wordmark__name { top: 216px; font-size: 37px; letter-spacing: 5px; }
  .wordmark__sub { top: 258px; font-size: 16px; letter-spacing: 9px; }
  .card--product .wordmark { top: 250px; font-size: 38px; color: var(--mark-cool); letter-spacing: 0; }

  .person {
    position: absolute;
    left: 0; right: 0;
    top: 404px;
  }
  .person__name { font-size: 27px; font-weight: 700; line-height: 1.2; }
  .person__first { color: var(--warm); }
  .person__last { color: var(--cool); }
  .person__title { font-size: 15px; margin-top: 3px; }

  .contact-divider {
    position: absolute;
    top: 472px;
    left: 100px;
    width: 164px;
    height: 20px;
  }
  .contact-details {
    position: absolute;
    left: 0; right: 0;
    top: 512px;
    font-size: 17px;
    line-height: 25px;
  }
  .rule {
    position: absolute;
    height: 1px;
    background: var(--rule);
  }
  .card--contact .rule { top: 582px; left: 98px; width: 168px; }

  .tagline {
    position: absolute;
    left: 0; right: 0;
    top: 500px;
    font-size: 17px;
    line-height: 22px;
    color: var(--sky);
  }
  .card--product .rule { top: 559px; left: 77px; width: 211px; }
  .website {
    position: absolute;
    left: 0; right: 0;
    top: 570px;
    font-size: 17px;
    color: var(--grey-text);
  }
</style>
</head>
<body>
  <section class="card card--contact" aria-label="Contact side">
    <span class="brand-dot"></span>
    <div class="wordmark wordmark__name">QUORVEL</div>
    <div class="wordmark wordmark__sub">LANGUAGE</div>

    <div class="person">
      <div class="person__name"><span class="person__first">Perry</span> <span class="person__last">Hollins</span></div>
      <div class="person__title">Founder &amp; CEO</div>
    </div>

    <svg class="contact-divider" viewBox="0 0 164 20" aria-hidden="true">
      <line x1="0" y1="10" x2="62" y2="10" stroke="#5a5a5a" stroke-width="1"/>
      <line x1="102" y1="10" x2="164" y2="10" stroke="#5a5a5a" stroke-width="1"/>
      <circle cx="71" cy="10" r="9" fill="#fff"/>
      <path d="M67 6 q-1 4 3 8 q4 3 8 2 l-1 -2 l-3 0 q-3 -2 -4 -5 l0 -3 z" fill="#000"/>
      <circle cx="93" cy="10" r="9" fill="#fff"/>
      <rect x="87.5" y="6" width="11" height="8" fill="none" stroke="#000" stroke-width="1.3"/>
      <path d="M87.5 6 L93 11 L98.5 6" fill="none" stroke="#000" stroke-width="1.3"/>
    </svg>

    <div class="contact-details">
      <div class="contact-details__phone">(555)-014-2736</div>
      <div class="contact-details__email">phollins@mailtrove.example</div>
    </div>
    <div class="rule"></div>
  </section>

  <section class="card card--product" aria-label="Product side">
    <span class="brand-dot"></span>
    <div class="wordmark">Lumidrasc</div>

    <p class="tagline">Culturally Immersive<br>Language Learning Games</p>
    <div class="rule"></div>
    <div class="website">www.lumidrasc.example</div>
  </section>
</body>
</html>
```